Lomira Vale Premium Full Spectrum CBD Oil

We want to launch a premium CBD oil product in several markets in Europe via an e-commerce platform. We want to create a brand that breathes quality and security. Simple design that stands out: little or no colours, original text formatting (see first three examples). Our brand is called Lomira Vale and we will launch a number of products: TORVease, TORVclear, TORVhold. We have some designs already made up but I find them too colourful, not classy enough. Is want more of a old school, black & white look, apothecary feel.... A logo is not needed to be recognizable... I add 6 designs to show what we have but this is NOT GOOD for me. You can copy the text on the label of course. PLease could you send me very clean and simple design that sticks and is very recognizable. I also add the text that should be added on the labels as the last attachment.
Target Market(s)
Europe - e-commerce: The Netherlands, Germany, France
Colors
Designer to choose only greyscale colors for use in the design.
Look and feel
Each slider illustrates characteristics of the customer's brand and the style your logo design should communicate.

```html
<!DOCTYPE html>
<html lang="en">
<head>
<meta charset="utf-8">
<title>Lomira Vale – Premium CBD Oil Label</title>
<link href="https://fonts.googleapis.com/css2?family=Abril+Fatface&family=Lato:wght@300;400;700&display=swap" rel="stylesheet">
<style>
  :root {
    --backdrop: #d2d2d2;
    --label: #ffffff;
    --ink: #1a1a1a;
    --ink-soft: #5a5a5a;
    --rule: #2a2a2a;
  }
  * { margin: 0; padding: 0; box-sizing: border-box; }
  html, body {
    width: 1200px;
    height: 801px;
    overflow: hidden;
    background: var(--backdrop);
  }
  .canvas {
    position: relative;
    width: 1200px;
    height: 801px;
    background: var(--backdrop);
  }
  .label {
    position: absolute;
    left: 385px;
    top: 46px;
    width: 430px;
    height: 710px;
    background: var(--label);
    color: var(--ink);
    font-family: "Lato", sans-serif;
    text-align: center;
  }
  .label > p {
    position: absolute;
    left: 0;
    width: 100%;
    height: 40px;
    line-height: 40px;
    white-space: nowrap;
  }
  .brand-name {
    top: 77px;
    font-weight: 300;
    font-size: 30px;
    letter-spacing: 1px;
  }
  .product-box {
    position: absolute;
    left: 52px;
    top: 171px;
    width: 326px;
    height: 281px;
    border: 1.5px solid var(--rule);
  }
  .grade {
    height: 68px;
    line-height: 66px;
    border-bottom: 1.5px solid var(--rule);
    font-weight: 400;
    font-size: 20px;
    letter-spacing: 9px;
    padding-left: 9px;
  }
  .product-type {
    position: absolute;
    left: 0;
    top: 118px;
    width: 100%;
    height: 62px;
    line-height: 62px;
    font-family: "Abril Fatface", serif;
    font-weight: 400;
    font-size: 56px;
  }
  .product-line {
    position: absolute;
    left: 0;
    top: 212px;
    width: 100%;
    height: 40px;
    line-height: 40px;
    font-size: 32px;
  }
  .line-prefix { font-weight: 700; }
  .line-suffix { font-weight: 300; }
  .spectrum-type {
    top: 498px;
    font-size: 20px;
    letter-spacing: 3px;
    color: var(--ink-soft);
  }
  .strength {
    top: 552px;
    font-size: 23px;
    letter-spacing: 2px;
  }
  .volume {
    top: 622px;
    font-size: 25px;
    letter-spacing: 3px;
    font-weight: 300;
    color: var(--ink-soft);
  }
</style>
</head>
<body>
  <main class="canvas">
    <section class="label">
      <p class="brand-name">Lomira Vale</p>

      <div class="product-box">
        <p class="grade">PREMIUM</p>
        <h1 class="product-type">CBD OIL</h1>
        <p class="product-line"><span class="line-prefix">TORV</span><span class="line-suffix">ease</span></p>
      </div>

      <p class="spectrum-type">FULL SPECTRUM</p>
      <p class="strength">1000 mg</p>
      <p class="volume">30 ml</p>
    </section>
  </main>
</body>
</html>
```